Dr Colin Pemberly needs a logo for letter head and business cards

I need a logo design for my stationery (letter head & business card). I am a Respiratory and Sleep medicine doctor who treats adults.
I treat asthma, snoring and other breathing problems and the symbols could include something relating to this. examples: ZZZ or a bed etc for snoring/sleep, a symbol of lungs , or other option. The blue lung could include a small red circle in the left one to indicate lung cancer.

Ideally in blue or green colour with maybe a small amount of red to indicate illness in the lung or somehow related to sleep.

the second side of the business card could include the text below:

Your next appointment is:
On ________________at_______________AM/PM

Please call to reschedule if necessary.

Target Market(s)

Middle aged to elderly patients and other medical staff. Professional context.

Industry/Entity Type

Medical

Contact Information for Business Card

Dr Colin Pemberly
MBBS (hons),
FRACP (Sleep & Respiratory).
DTM&H, MHSM, GC-CU.
www.harwoodclinicians.example

Locations:
Kestrel Private Specialist Consulting Rooms,
Level1, 517 Durnford Road,
Oakmere VIC 3187
Ph: 9461 7053
Fax: 8315 6640

Logo Text

that this is a respectable and trustworthy medical specialist

Font styles to use
Sans Serif

Colors
34a6d7
0655a3
33b8a4
00a88f
85cae6
ec1f27

Requirements
Must have
• my name in the logo . I have included my current business card and need to replace the logo/wording in the top right corner "Kestrel Private specialist Consulting Rooms" for my own personalised logo.
Nice to have
• symbol relating to lungs /breathing and sleep
Should not have
• Should not have the location in the logo of the business card

```html
<!DOCTYPE html>
<html lang="en">
<head>
<meta charset="utf-8">
<title>Dr Colin Pemberly – Stationery</title>
<link rel="stylesheet" href="https://fonts.googleapis.com/css2?family=Encode+Sans+Semi+Condensed:wght@400;500;700&display=swap">
<style>
:root{
  --board:#1f1b1a;
  --paper:#ffffff;
  --blue:#0a90da;
  --green:#43b195;
  --red:#e3242b;
  --ink:#4a4a4a;
}
*{margin:0;padding:0;box-sizing:border-box}
html,body{width:1200px;height:1038px;overflow:hidden;background:var(--board)}
body{position:relative;font-family:"Encode Sans Semi Condensed",sans-serif;color:var(--ink)}
.sheet{position:absolute;background:var(--paper);overflow:hidden}
.logo-sheet{left:54px;top:37px;width:391px;height:476px}
.letterhead{left:466px;top:37px;width:681px;height:962px}
.business-card{left:57px;top:532px;width:386px;height:226px}
.appointment-card{left:57px;top:773px;width:386px;height:226px}

.wordmark{position:absolute;color:var(--blue);font-weight:500;line-height:.9;text-align:center}
.wordmark .line{display:block;white-space:nowrap}
.wordmark .dot{display:inline-block;border-radius:50%;background:var(--red);vertical-align:middle}
.wordmark-lg{left:0;right:0;top:200px;font-size:84px}
.wordmark-lg .dot{width:16px;height:16px;margin-left:10px}
.wordmark-lg .line + .line{font-size:72px;margin-top:8px}
.wordmark-sm{font-size:30px}
.wordmark-sm .line + .line{font-size:26px;margin-top:2px}
.wordmark-sm .dot{width:7px;height:7px;margin-left:4px}

.block{position:absolute;background:var(--green)}
.name{position:absolute;color:var(--green);font-weight:400;white-space:nowrap}
.creds{position:absolute;font-size:9px;line-height:12px;color:var(--ink)}

.letterhead .corner-block{left:0;top:0;width:124px;height:142px;border-radius:0 0 10px 0}
.letterhead .name{left:150px;top:58px;font-size:17px}
.letterhead .creds{left:150px;top:80px;color:#666}
.letterhead .wordmark-sm{right:27px;top:826px;text-align:right;font-size:40px}
.letterhead .wordmark-sm .line + .line{font-size:34px}
.letterhead .footer{position:absolute;right:27px;top:912px;font-size:10.5px;line-height:14px;text-align:right;color:#666}

.business-card .wordmark-sm{left:29px;top:26px;text-align:left}
.business-card .side-block{left:274px;top:20px;width:106px;height:200px;border-radius:60px 14px 14px 22px}
.business-card .edge{left:378px;top:0;width:8px;height:85px}
.business-card .contact{position:absolute;right:23px;top:144px;font-size:9.6px;line-height:12px;text-align:right;color:#fff}
.business-card .name{left:24px;top:150px;font-size:16px}
.business-card .creds{left:24px;top:172px}

.appointment-card .side-block{left:7px;top:18px;width:107px;height:202px;border-radius:40px 60px 22px 22px}
.appointment-card .edge{left:0;top:0;width:9px;height:90px}
.appointment-card .prompt{position:absolute;left:18px;top:102px;color:#fff;font-weight:700;font-size:11.5px;line-height:12px;text-transform:uppercase}
.appointment-card .url{position:absolute;left:73px;top:10px;font-size:10px;font-style:italic;color:var(--green)}
.appointment-card .wordmark-sm{right:16px;top:15px;text-align:right;font-size:24px}
.appointment-card .wordmark-sm .line + .line{font-size:21px}
.slots{position:absolute;left:151px;top:72px;width:216px;list-style:none;color:var(--green);font-size:11px}
.slots li{display:flex;align-items:baseline;height:32.3px}
.slots .rule{border-bottom:1px solid var(--green);height:1px;align-self:flex-end;margin-bottom:20px}
.slots .r1{width:72px}.slots .r2{width:82px}
.appointment-card .note{position:absolute;right:19px;top:200px;font-size:9.5px;color:var(--green)}
</style>
</head>
<body>

<section class="sheet logo-sheet">
  <div class="wordmark wordmark-lg">
    <span class="line">Dr COLIN<span class="dot"></span></span>
    <span class="line">PEMBERLY</span>
  </div>
</section>

<section class="sheet letterhead">
  <div class="block corner-block" role="img" aria-label="Green lung illustration"></div>
  <div class="name">Dr Colin Pemberly</div>
  <div class="creds">MBBS(Hon),<br>FRACP(Sleep &amp; Respiratory),<br>DTM&amp;H</div>
  <div class="wordmark wordmark-sm">
    <span class="line">Dr COLIN<span class="dot"></span></span>
    <span class="line">PEMBERLY</span>
  </div>
  <div class="footer">517 Durnford Road, Oakmere Vic 3187<br>Tel: 9461 7053 &nbsp;|&nbsp; Fax: 8315 6640</div>
</section>

<section class="sheet business-card">
  <div class="wordmark wordmark-sm">
    <span class="line">Dr COLIN<span class="dot"></span></span>
    <span class="line">PEMBERLY</span>
  </div>
  <div class="block edge"></div>
  <div class="block side-block" role="img" aria-label="Green lung illustration"></div>
  <div class="contact">517 Durnford Road<br>Oakmere Vic 3187<br>Tel: 9461 7053<br>Fax: 8315 6640</div>
  <div class="name">Dr Colin Pemberly</div>
  <div class="creds">MBBS(Hon),<br>FRACP(Sleep &amp; Respiratory),<br>DTM&amp;H</div>
</section>

<section class="sheet appointment-card">
  <div class="block edge"></div>
  <div class="block side-block" role="img" aria-label="Green lung illustration"></div>
  <div class="prompt">Your<br>next<br>appointment<br>is:</div>
  <div class="url">www.kestrelprivate.example</div>
  <div class="wordmark wordmark-sm">
    <span class="line">Dr COLIN<span class="dot"></span></span>
    <span class="line">PEMBERLY</span>
  </div>
  <ul class="slots">
    <li>On<span class="rule r1"></span>at<span class="rule r2"></span>AM/PM</li>
    <li>On<span class="rule r1"></span>at<span class="rule r2"></span>AM/PM</li>
    <li>On<span class="rule r1"></span>at<span class="rule r2"></span>AM/PM</li>
    <li>On<span class="rule r1"></span>at<span class="rule r2"></span>AM/PM</li>
  </ul>
  <div class="note">Please call to reschedule if necessary</div>
</section>

</body>
</html>
```